Business Card Makeover. Recreate a sleek modern design for our business card.

DO NOT COPY OUR CURRENT DESIGN. MUST BE ONE SIDED BUSINESS CARD.
Create a new business card design, using our new logo. Attached is a sample of our current design and new logo. Please note the address and email will change. The new address is 417 Corvell West Palm Beach 33472 and our website will be www.talvendrake.example.

We are an architectural and interior design firm. We prefer a clean modern look. Something that is refined and emulates excellence.

Industry/Entity Type

Architecture

Contact Information for Business Card

clean modern look, please do not copy our attached design.

Font styles to use
Other font styles liked:
• see attached business card font

Colors

Designer to choose colors to be used in the design.

Requirements
Must have
• Must have a modern appeal and resemble our current branding.
Nice to have
• modern font, our logo, legible name and titles progressive design
Should not have
• Do not add colors not reflected in our branding. Should not look like our current card.

```html
<!DOCTYPE html>
<html lang="en">
<head>
<meta charset="utf-8">
<title>Talvendrake + Partners — Business Card</title>
<link rel="stylesheet" href="https://fonts.googleapis.com/css2?family=Roboto:wght@300;400;700&family=Roboto+Condensed:wght@400;700&display=swap">
<style>
  :root {
    --page: #e9eaec;
    --card: #ffffff;
    --blue: #0a73c9;
    --blue-deep: #065fae;
    --blue-soft: #4a95d6;
    --blue-pale: #74b3e6;
    --charcoal: #363435;
    --ink: #1d1d1f;
    --white: #ffffff;
  }
  * { margin: 0; padding: 0; box-sizing: border-box; }
  html, body { width: 1200px; height: 840px; overflow: hidden; background: var(--page); }
  .business-card {
    position: absolute; left: 75px; top: 120px;
    width: 1050px; height: 600px;
    background: var(--card);
    overflow: hidden;
    box-shadow: 0 10px 30px rgba(0,0,0,.12);
    font-family: "Roboto", Arial, sans-serif;
  }
  .card-art { position: absolute; inset: 0; }
  .brand {
    position: absolute; left: 250px; top: 82px;
    display: flex; align-items: center; gap: 20px;
  }
  .brand-dot { width: 80px; height: 80px; border-radius: 50%; background: var(--blue); }
  .brand-name {
    font-family: "Roboto", Arial, sans-serif;
    font-weight: 300; font-size: 34px; letter-spacing: 3px;
    color: var(--ink); white-space: nowrap;
  }
  .person { position: absolute; left: 150px; top: 250px; }
  .person-name {
    font-family: "Roboto Condensed", Arial, sans-serif;
    font-weight: 700; font-size: 36px; color: var(--blue); white-space: nowrap;
  }
  .person-title { font-size: 25px; color: var(--ink); margin-top: 2px; }
  .contact { position: absolute; left: 150px; top: 372px; font-size: 24px; line-height: 36px; color: var(--ink); white-space: nowrap; }
  .contact-label { font-family: "Roboto Condensed", Arial, sans-serif; font-weight: 700; color: var(--blue); }
  .address {
    position: absolute; right: 40px; top: 318px;
    text-align: right; color: var(--white);
    font-size: 23px; line-height: 32px; white-space: nowrap;
  }
  .license { font-family: "Roboto Condensed", Arial, sans-serif; font-weight: 700; font-size: 25px; margin-top: 12px; }
  .services {
    position: absolute; left: 0; right: 0; bottom: 0; height: 86px;
    display: flex; align-items: center; justify-content: center;
    color: var(--white); font-weight: 700; font-size: 28px; letter-spacing: 15px;
  }
</style>
</head>
<body>
  <div class="business-card">
    <svg class="card-art" width="1050" height="600" viewBox="0 0 1050 600" aria-hidden="true">
      <defs>
        <linearGradient id="mist-fade" x1="0" y1="0" x2="1" y2="1">
          <stop offset="0" stop-color="#ffffff"/>
          <stop offset="1" stop-color="#d9dbdd"/>
        </linearGradient>
        <linearGradient id="blue-sweep" x1="0" y1="0" x2="1" y2="1">
          <stop offset="0" stop-color="#0a73c9"/>
          <stop offset="1" stop-color="#4a95d6"/>
        </linearGradient>
      </defs>
      <rect width="1050" height="600" fill="url(#mist-fade)"/>
      <path d="M0 0 H300 C170 80 110 240 125 514 H0 Z" fill="url(#blue-sweep)"/>
      <path d="M300 0 C170 80 110 240 125 514 L150 514 C140 260 190 110 330 0 Z" fill="#ffffff" opacity=".85"/>
      <circle cx="1000" cy="620" r="440" fill="var(--blue-deep)"/>
      <circle cx="1020" cy="620" r="410" fill="url(#blue-sweep)"/>
      <circle cx="990" cy="470" r="190" fill="var(--blue-pale)" opacity=".3"/>
      <rect x="0" y="514" width="1050" height="86" fill="var(--charcoal)"/>
    </svg>

    <div class="brand">
      <div class="brand-dot"></div>
      <div class="brand-name">TALVENDRAKE + PARTNERS</div>
    </div>

    <div class="person">
      <div class="person-name">Mara Ellison, AIA, LEED® AP</div>
      <div class="person-title">Partner Project Architect</div>
    </div>

    <div class="contact">
      <div><span class="contact-label">office:</span> 561.555.0142</div>
      <div><span class="contact-label">fax:</span> 561.555.0178</div>
      <div><span class="contact-label">web:</span> www.talvendrake.example</div>
    </div>

    <div class="address">
      <div>417 Corvell</div>
      <div>West Palm Beach, FL 33472</div>
      <div class="license">LIC.# AA26009187</div>
    </div>

    <div class="services">ARCHITECTURE + INTERIOR DESIGN</div>
  </div>
</body>
</html>
```